Coffee Package Design

We need a new package design for a coffee company. Need to be a mix between modern and classic design combined together. We are open to different ideas.
We changing our product name from Café Verlona to Café Rostelli. The picture upload
shows what the product looks like. We want something completely different. The name of the company should go on the back of the package.
Updates

Hello Everyone,

Please read description, we are going with a new name and design for the product.

Café Rostelli. Café Verlona is what we are replacing with Café Rostelli, we are looking for new

look and design, please submit new designs.

There is a change in the description. Please take out Premium coffee blend and replace with Italian Roast.                                    

Industry/Entity Type

Cafe

Requirements
Must have
• You can use up to 6 colors.
Please put these items on design: Café Rostelli (this is the product name), Regular Premium Blend Coffee, 100% Arabica,
Dumbrell & Sons (name of the company), Tyler, TX on the back of the package

The file uploaded is an example of one of our products and how the package film
is sized.

```html
<!DOCTYPE html>
<html lang="en">
<head>
<meta charset="utf-8">
<title>Café Rostelli – Regular Sachet</title>
<link rel="stylesheet" href="https://fonts.googleapis.com/css2?family=Open+Sans:wght@400;600&family=Roboto+Condensed:wght@700&display=swap">
<style>
  :root {
    --stage: #d9d4cc;
    --film: #2e1a1b;
    --film-seal: #281617;
    --seal-line: #1d0f10;
    --cream: #ece4d6;
    --ornament: #cfc4b2;
    --ink: #2e1a1b;
    --text-light: #d8d0c6;
    --teal: #1f9b8c;
  }
  * { margin: 0; padding: 0; box-sizing: border-box; }
  html, body {
    width: 1200px;
    height: 960px;
    overflow: hidden;
    background: var(--stage);
  }
  .canvas {
    position: relative;
    width: 1200px;
    height: 960px;
  }
  .sachet-art {
    position: absolute;
    left: 0;
    top: 0;
  }
  .sachet-film { fill: var(--film); }
  .sachet-seal { fill: var(--film-seal); }
  .seal-line { stroke: var(--seal-line); stroke-width: 2; }
  .hang-slot { fill: none; stroke: var(--seal-line); stroke-width: 2; }
  .medallion-ornament { fill: var(--ornament); }
  .medallion-face { fill: var(--cream); }

  .medallion-name {
    position: absolute;
    left: 470px;
    top: 420px;
    width: 260px;
    text-align: center;
    font-family: "Open Sans", sans-serif;
    font-weight: 600;
    font-size: 34px;
    line-height: 1;
    color: var(--ink);
  }
  .product-line {
    position: absolute;
    left: 400px;
    width: 400px;
    text-align: center;
    color: var(--text-light);
    font-family: "Open Sans", sans-serif;
    font-weight: 400;
    line-height: 1.2;
    white-space: nowrap;
  }
  .product-line--roast { top: 622px; font-size: 26px; letter-spacing: 1.5px; }
  .product-line--origin { top: 656px; font-size: 18px; }

  .variety {
    position: absolute;
    left: 498px;
    top: 694px;
    width: 218px;
    height: 40px;
    display: flex;
    align-items: center;
    justify-content: space-between;
  }
  .variety-tail { display: block; width: 18px; height: 22px; }
  .variety-tail path { fill: var(--teal); }
  .variety-label {
    font-family: "Roboto Condensed", sans-serif;
    font-weight: 700;
    font-size: 36px;
    line-height: 1;
    color: var(--teal);
    letter-spacing: 0.5px;
  }
</style>
</head>
<body>
<main class="canvas">
  <svg class="sachet-art" width="1200" height="960" viewBox="0 0 1200 960">
    <defs>
      <pattern id="serration" x="325" y="0" width="8" height="10" patternUnits="userSpaceOnUse">
        <path d="M0 10 L4 0 L8 10 Z" fill="#281617"/>
      </pattern>
      <pattern id="serration-bottom" x="325" y="0" width="8" height="10" patternUnits="userSpaceOnUse">
        <path d="M0 0 L4 10 L8 0 Z" fill="#281617"/>
      </pattern>
    </defs>

    <g class="sachet">
      <rect class="sachet-film" x="325" y="142" width="552" height="674"/>
      <rect x="325" y="132" width="552" height="10" fill="url(#serration)"/>
      <rect x="325" y="816" width="552" height="10" fill="url(#serration-bottom)"/>

      <rect class="sachet-seal" x="325" y="142" width="552" height="70"/>
      <g class="seal-lines">
        <line class="seal-line" x1="325" y1="150" x2="877" y2="150"/>
        <line class="seal-line" x1="325" y1="160" x2="877" y2="160"/>
        <line class="seal-line" x1="325" y1="198" x2="877" y2="198"/>
        <line class="seal-line" x1="325" y1="208" x2="877" y2="208"/>
      </g>
      <path class="hang-slot" d="M550 186 L555 178 H646 L651 186 L646 194 H555 Z"/>

      <rect class="sachet-seal" x="325" y="760" width="552" height="56"/>
      <g class="seal-lines">
        <line class="seal-line" x1="325" y1="768" x2="877" y2="768"/>
        <line class="seal-line" x1="325" y1="778" x2="877" y2="778"/>
        <line class="seal-line" x1="325" y1="800" x2="877" y2="800"/>
        <line class="seal-line" x1="325" y1="810" x2="877" y2="810"/>
      </g>
    </g>

    <g class="medallion">
      <path class="medallion-ornament" role="img" aria-label="Ornate filigree scroll frame around the product medallion"
            fill-rule="evenodd"
            d="M600 262 A176 176 0 1 1 599.9 262 Z M600 290 A148 148 0 1 0 600.1 290 Z" opacity="0.55"/>
      <circle class="medallion-face" cx="600" cy="438" r="134"/>
    </g>
  </svg>

  <p class="medallion-name">Café Rostelli</p>

  <p class="product-line product-line--roast">Italian Roast</p>
  <p class="product-line product-line--origin">100% Arabica</p>

  <div class="variety">
    <svg class="variety-tail" viewBox="0 0 18 22"><path d="M0 0 H18 V22 H0 L7 11 Z"/></svg>
    <span class="variety-label">REGULAR</span>
    <svg class="variety-tail" viewBox="0 0 18 22"><path d="M0 0 H18 L11 11 L18 22 H0 Z"/></svg>
  </div>
</main>
</body>
</html>
```